Business Card Project for Firm Deck Hoisting

Business name is "Firm Deck Hoisting" we are a scaffolding & rigging business specialising in local and remote work for:
- scaffolding (residential, commercial, industrial)
- rigging
-man material hoists
- swing stages
- labour hire

On the back of the card I would like FDH as the symbol / logo. I have attached the logos we have had created by sketch harbour. We would like to use bold colours – preferably as the same colour scheme as the logo.

Target Market(s)

Construction business

Industry/Entity Type

Construction

Contact Information for Business Card

name: Owen Pellew
Title: Director
Phone: 0491 572 864
Address: PO BOX 3251, Brindle Vale SA 5094
Email: owen@firmdeckhoisting.com.au
Website: www.firmdeckhoisting.com.au

Font styles to use
Sans Serif

Requirements
Must have
• Must use existing logo & prefering using bold colours
Nice to have
• Would be nice to have a line of dot points in what we specialise in but not essential
• Would be nice to see some designs with a slogan but not essential
Should not have
• NA

```html
<!DOCTYPE html>
<html lang="en">
<head>
<meta charset="utf-8">
<title>Firm Deck Hoisting – Business Card</title>
<link rel="stylesheet" href="https://fonts.googleapis.com/css2?family=Source+Sans+3:wght@400;600;700&display=swap">
<style>
  :root {
    --brand-blue: #1665a8;
    --band-blue: #1a6ab0;
    --ink: #1f1f1f;
    --ink-soft: #333333;
    --paper: #eceded;
    --backdrop: #e4e4e4;
    --black: #0c0c0c;
    --white: #ffffff;
  }
  * { box-sizing: border-box; margin: 0; padding: 0; }
  html, body {
    width: 1105px; height: 1200px; overflow: hidden;
    background: var(--backdrop);
    font-family: "Source Sans 3", sans-serif;
  }
  .canvas { position: relative; width: 1105px; height: 1200px; }

  .card {
    position: absolute; left: 182px; width: 746px; height: 425px; overflow: hidden;
  }
  .card--front { top: 119px; background: var(--paper); }
  .card--back { top: 637px; background: var(--brand-blue); }

  /* front */
  .brand {
    position: absolute; left: 58px; top: 190px;
    display: flex; align-items: center; gap: 10px;
  }
  .brand__square { width: 16px; height: 16px; background: var(--brand-blue); }
  .brand__name {
    font-weight: 700; font-size: 29px; color: var(--ink); letter-spacing: 0.2px;
  }

  .contact { position: absolute; left: 394px; top: 106px; color: var(--ink-soft); }
  .contact__name {
    font-weight: 600; font-size: 27px; color: var(--brand-blue); line-height: 1; letter-spacing: 0.3px;
  }
  .contact__title { font-weight: 600; font-size: 19px; color: var(--ink); margin-top: 6px; }
  .contact__address { font-size: 19px; line-height: 27px; margin-top: 12px; }
  .contact__line {
    display: flex; align-items: center; gap: 10px; font-size: 19px; line-height: 29px;
  }
  .contact__line:first-of-type { margin-top: 18px; }
  .contact__icon { width: 16px; height: 16px; fill: var(--brand-blue); flex: none; }

  .footer-bar { position: absolute; left: 0; bottom: 0; width: 746px; height: 45px; }
  .website {
    position: absolute; right: 26px; bottom: 10px;
    font-size: 19px; color: var(--white); letter-spacing: 0.2px;
  }

  /* back */
  .back-mark {
    position: absolute; left: 0; right: 0; top: 138px; text-align: center;
    font-weight: 700; font-size: 124px; line-height: 1; color: var(--paper); letter-spacing: 4px;
  }
  .services {
    position: absolute; left: 0; right: 0; top: 332px; text-align: center;
    color: var(--paper); font-weight: 600; font-size: 20px; line-height: 26px;
  }
</style>
</head>
<body>
<main class="canvas">
  <section class="card card--front" aria-label="Business card front">
    <div class="brand">
      <span class="brand__square"></span>
      <span class="brand__name">Firm Deck Hoisting</span>
    </div>

    <div class="contact">
      <p class="contact__name">OWEN PELLEW</p>
      <p class="contact__title">DIRECTOR</p>
      <p class="contact__address">PO BOX 3251<br>Brindle Vale SA 5094</p>
      <p class="contact__line">
        <svg class="contact__icon" viewBox="0 0 24 24" aria-hidden="true"><path d="M6.6 10.8a15.1 15.1 0 0 0 6.6 6.6l2.2-2.2a1 1 0 0 1 1-.25 11.4 11.4 0 0 0 3.6.57 1 1 0 0 1 1 1V20a1 1 0 0 1-1 1A17 17 0 0 1 3 4a1 1 0 0 1 1-1h3.5a1 1 0 0 1 1 1c0 1.25.2 2.45.57 3.57a1 1 0 0 1-.25 1z"/></svg>
        0491 572 864
      </p>
      <p class="contact__line">
        <svg class="contact__icon" viewBox="0 0 24 24" aria-hidden="true"><path d="M2 5h20v14H2z M3.5 6.5 12 13l8.5-6.5" fill="none" stroke="var(--brand-blue)" stroke-width="2"/><path d="M2 5h20L12 12.5z"/></svg>
        owen@firmdeckhoisting.com.au
      </p>
    </div>

    <svg class="footer-bar" viewBox="0 0 746 45" aria-hidden="true">
      <rect x="0" y="30" width="384" height="15" fill="var(--black)"/>
      <polygon points="376,45 412,0 746,0 746,45" fill="var(--band-blue)"/>
    </svg>
    <p class="website">www.firmdeckhoisting.com.au</p>
  </section>

  <section class="card card--back" aria-label="Business card back">
    <p class="back-mark">FDH</p>
    <p class="services">
      Scaffolding (Residential, Commercial, Industrial)<br>
      Rigging • Man material hoists • Swing stages • Labour hire
    </p>
  </section>
</main>
</body>
</html>
```